Label for a new Bourbon bottle

Name of the new Bourbon is Bolado. This will be a Straight Bourbon Finished in Sherry Casks. We are calling in Bolado to give it the look and feel of Spanish and Portuguese influence where sherry comes from. I've included some samples of labels in the US, you can also take a look at Spanish sherry bottle labels included too and get some inspiration, it can have traditional influence but with it's own style, not too focused on barrels. The proof will be 90, alc. by vol. 45%. Volume 750 ML.

Target Market(s)

Whiskey and Bourbon drinkers

Requirements
Must have
• Elegant, classy but not a mirror of what so many traditional labels look like, must feel high-end, expensive

```html
<!DOCTYPE html>
<html lang="en">
<head>
<meta charset="utf-8">
<title>Bolado Straight Bourbon – Label</title>
<link href="https://fonts.googleapis.com/css2?family=Rye&family=IM+Fell+English+SC&family=Playfair+Display+SC:wght@700&family=Germania+One&display=swap" rel="stylesheet">
<style>
  :root {
    --paper: #dfdbc4;
    --ink: #231815;
    --ink-soft: #6b5f54;
    --cream: #f3ead8;
    --page: #ffffff;
  }
  html, body {
    margin: 0;
    padding: 0;
    width: 1200px;
    height: 1200px;
    overflow: hidden;
    background: var(--page);
  }
  .canvas {
    position: relative;
    width: 1200px;
    height: 1200px;
  }
  .label {
    position: absolute;
    left: 81px;
    top: 107px;
    width: 1025px;
    height: 996px;
    background: var(--paper);
  }
  .label-art {
    position: absolute;
    inset: 0;
  }
  .ornament {
    position: absolute;
    background: radial-gradient(ellipse at center, rgba(35,24,21,0.22), rgba(35,24,21,0.04) 70%, transparent);
    border-radius: 50%;
  }
  .ornament--crown { left: 313px; top: 68px; width: 412px; height: 81px; }
  .ornament--whiskey-left { left: 293px; top: 547px; width: 40px; height: 80px; }
  .ornament--whiskey-right { left: 705px; top: 547px; width: 40px; height: 80px; }
  .ornament--lower { left: 172px; top: 637px; width: 691px; height: 94px; }

  .brand-name {
    position: absolute;
    left: 0;
    top: 205px;
    width: 1025px;
    margin: 0;
    text-align: center;
    font-family: "Rye", serif;
    font-weight: 400;
    font-size: 182px;
    line-height: 1;
    letter-spacing: 4px;
    color: var(--cream);
    -webkit-text-stroke: 5px var(--ink);
    paint-order: stroke fill;
    text-shadow: 8px 8px 0 var(--ink);
    text-transform: uppercase;
  }
  .style-line {
    position: absolute;
    left: 338px;
    top: 449px;
    width: 519px;
    margin: 0;
    text-align: center;
    font-family: "IM Fell English SC", serif;
    font-size: 62px;
    line-height: 1;
    color: var(--ink);
    letter-spacing: 1px;
  }
  .spirit-type {
    position: absolute;
    left: 331px;
    top: 561px;
    width: 372px;
    margin: 0;
    text-align: center;
    font-family: "Playfair Display SC", serif;
    font-weight: 700;
    font-size: 38px;
    line-height: 1;
    letter-spacing: 3px;
    color: var(--ink);
  }
  .seal {
    position: absolute;
    width: 144px;
    height: 144px;
    display: flex;
    align-items: center;
    justify-content: center;
    text-align: center;
    font-family: "Germania One", sans-serif;
    font-size: 24px;
    line-height: 1.05;
    color: var(--ink);
  }
  .seal--abv { left: 75px; top: 777px; }
  .seal--proof { left: 822px; top: 777px; }
  .volume {
    position: absolute;
    left: 0;
    top: 888px;
    width: 1025px;
    margin: 0;
    text-align: center;
    font-family: "Germania One", sans-serif;
    font-size: 44px;
    line-height: 1;
    color: var(--ink);
  }
  .cask-finish {
    font-family: "Germania One", sans-serif;
    font-size: 38px;
    letter-spacing: 1px;
    fill: var(--ink);
  }
</style>
</head>
<body>
<div class="canvas">
  <section class="label">
    <svg class="label-art" width="1025" height="996" viewBox="0 0 1025 996">
      <!-- frame -->
      <rect x="11" y="17" width="1003" height="968" fill="none" stroke="var(--ink)" stroke-width="4"/>
      <g role="img" aria-label="Repeating key pattern border">
        <path fill="var(--ink-soft)" fill-rule="evenodd"
          d="M18 24 H1007 V978 H18 Z M36 42 V960 H989 V42 Z"/>
      </g>
      <rect x="40" y="46" width="945" height="910" fill="none" stroke="var(--ink)" stroke-width="3"/>
      <rect x="45" y="51" width="935" height="900" fill="none" stroke="var(--ink)" stroke-width="1.5"/>

      <!-- divider under name -->
      <g class="divider" fill="var(--ink)" stroke="var(--ink)">
        <line x1="470" y1="415" x2="738" y2="415" stroke-width="3"/>
        <path d="M460 415 L476 407 L472 415 L476 423 Z"/>
        <path d="M748 415 L732 407 L736 415 L732 423 Z"/>
        <circle cx="677" cy="415" r="6"/>
      </g>

      <!-- whiskey rules -->
      <g stroke="var(--ink)" fill="none">
        <line x1="439" y1="540" x2="600" y2="540" stroke-width="1.5"/>
        <line x1="331" y1="547" x2="703" y2="547" stroke-width="1.5"/>
        <line x1="331" y1="613" x2="703" y2="613" stroke-width="1.5"/>
        <line x1="331" y1="619" x2="703" y2="619" stroke-width="1.5"/>
        <line x1="343" y1="568" x2="358" y2="568" stroke-width="2.5"/>
        <line x1="343" y1="578" x2="358" y2="578" stroke-width="2.5"/>
        <line x1="343" y1="588" x2="358" y2="588" stroke-width="2.5"/>
        <line x1="676" y1="568" x2="691" y2="568" stroke-width="2.5"/>
        <line x1="676" y1="578" x2="691" y2="578" stroke-width="2.5"/>
        <line x1="676" y1="588" x2="691" y2="588" stroke-width="2.5"/>
      </g>

      <!-- banner arcs -->
      <g stroke="var(--ink)" fill="none">
        <path d="M289 674 Q520 820 746 674" stroke-width="3"/>
        <path d="M226 716 Q520 920 810 716" stroke-width="1.5"/>
        <path d="M232 738 Q520 940 806 738" stroke-width="3"/>
      </g>
      <defs>
        <path id="cask-arc" d="M264 703 Q522 920 780 703"/>
      </defs>
      <text class="cask-finish" text-anchor="middle">
        <textPath href="#cask-arc" startOffset="50%">FINISHED IN SHERRY CASKS</textPath>
      </text>

      <!-- seals -->
      <g class="seal-shape" fill="var(--ink)">
        <circle cx="147" cy="849" r="72"/>
        <circle cx="147" cy="849" r="60" fill="var(--paper)"/>
        <circle cx="147" cy="849" r="56" fill="none" stroke="var(--ink)" stroke-width="1.5"/>
        <circle cx="894" cy="849" r="72"/>
        <circle cx="894" cy="849" r="60" fill="var(--paper)"/>
        <circle cx="894" cy="849" r="56" fill="none" stroke="var(--ink)" stroke-width="1.5"/>
      </g>
    </svg>

    <div class="ornament ornament--crown" role="img" aria-label="Scrolling flourish ornament"></div>
    <div class="ornament ornament--whiskey-left" role="img" aria-label="Small scroll ornament"></div>
    <div class="ornament ornament--whiskey-right" role="img" aria-label="Small scroll ornament"></div>
    <div class="ornament ornament--lower" role="img" aria-label="Wide scrolling flourish ornament"></div>

    <h1 class="brand-name">Bolado</h1>
    <p class="style-line">Straight Bourbon</p>
    <p class="spirit-type">WHISKEY</p>

    <div class="seal seal--abv">45%<br>ALC.VOL.</div>
    <div class="seal seal--proof">90<br>PROOF</div>
    <p class="volume">750 ML</p>
  </section>
</div>
</body>
</html>
```